Brennick Holdings Business Cards

These are professional business cards that are for my family office.
Put fake emails and phone numbers as of now until I finalize those components. This family office controls my families investments, assets, and future. The cards should be professional.
..
.
.
.
I just uploaded another variation of a logo I would like to see as a business card to I am inbeteen which logo to use

Target Market(s)

business

Industry/Entity Type

business

Contact Information for Business Card

Professional, wealth related, finance related.

Requirements
Must have
• Logo

```html
<!DOCTYPE html>
<html lang="en">
<head>
<meta charset="utf-8">
<title>Brennick Holdings – Business Cards</title>
<link rel="stylesheet" href="https://fonts.googleapis.com/css2?family=Cinzel:wght@500;600&family=Poppins:wght@400&display=swap">
<style>
  :root {
    --backdrop: #2b2b2b;
    --card-navy: #1a1f2e;
    --gold: #d8ba7a;
    --gold-edge: #e6cb8e;
    --card-shadow: rgba(0, 0, 0, 0.45);
  }
  * { box-sizing: border-box; margin: 0; padding: 0; }
  html, body {
    width: 1200px;
    height: 1015px;
    overflow: hidden;
    background: var(--backdrop);
  }
  .stage {
    position: relative;
    width: 1200px;
    height: 1015px;
  }
  .card {
    position: absolute;
    width: 560px;
    height: 320px;
    background: var(--card-navy);
    border-bottom: 3px solid var(--gold-edge);
    box-shadow: 0 14px 30px var(--card-shadow);
    color: var(--gold);
  }
  .card--front { left: 110px; top: 135px; }
  .card--back  { left: 530px; top: 535px; }

  /* Front */
  .front-mark {
    position: absolute;
    left: 50%;
    top: 48px;
    transform: translateX(-50%);
    width: 132px;
    height: 132px;
  }
  .front-name {
    position: absolute;
    left: 0;
    right: 0;
    top: 212px;
    text-align: center;
    font-family: "Cinzel", serif;
    font-weight: 600;
    font-size: 30px;
    letter-spacing: 1px;
  }

  /* Back */
  .back-mark {
    position: absolute;
    right: 48px;
    top: 58px;
    width: 196px;
    height: 196px;
  }
  .holder {
    position: absolute;
    left: 40px;
    top: 62px;
  }
  .holder-name {
    font-family: "Cinzel", serif;
    font-weight: 600;
    font-size: 23px;
    line-height: 1;
  }
  .holder-role {
    font-family: "Poppins", sans-serif;
    font-size: 12.5px;
    margin-top: 3px;
  }
  .contact-list {
    position: absolute;
    left: 40px;
    top: 150px;
    list-style: none;
    font-family: "Poppins", sans-serif;
    font-size: 12.5px;
  }
  .contact-item {
    display: flex;
    align-items: center;
    gap: 10px;
    height: 24px;
  }
  .contact-icon {
    width: 18px;
    height: 18px;
    flex: none;
  }
  .address {
    position: absolute;
    left: 68px;
    top: 246px;
    font-family: "Poppins", sans-serif;
    font-size: 12.5px;
    line-height: 1.35;
  }
</style>
</head>
<body>
<main class="stage">

  <section class="card card--front" aria-label="Business card front">
    <svg class="front-mark" viewBox="0 0 132 132" aria-hidden="true">
      <circle cx="66" cy="66" r="62" fill="none" stroke="var(--gold)" stroke-width="2.5"/>
    </svg>
    <h1 class="front-name">Brennick Holdings</h1>
  </section>

  <section class="card card--back" aria-label="Business card back">
    <div class="holder">
      <h2 class="holder-name">Adrian Hale</h2>
      <p class="holder-role">Managing Director</p>
    </div>

    <ul class="contact-list">
      <li class="contact-item">
        <svg class="contact-icon" viewBox="0 0 18 18" aria-hidden="true">
          <circle cx="9" cy="9" r="9" fill="var(--gold)"/>
          <path d="M6 5.2l1.6-.3.9 2-1 .8a6 6 0 0 0 2.8 2.8l.8-1 2 .9-.3 1.6c-3.6.3-7.1-3.2-6.8-6.8z" fill="var(--card-navy)"/>
        </svg>
        <span>044-318 902 574</span>
      </li>
      <li class="contact-item">
        <svg class="contact-icon" viewBox="0 0 18 18" aria-hidden="true">
          <circle cx="9" cy="9" r="9" fill="var(--gold)"/>
          <rect x="4.5" y="6" width="9" height="6.2" fill="var(--card-navy)"/>
          <path d="M4.8 6.3L9 9.6l4.2-3.3" fill="none" stroke="var(--gold)" stroke-width="0.9"/>
        </svg>
        <span>office@brennickholdings.com</span>
      </li>
      <li class="contact-item">
        <svg class="contact-icon" viewBox="0 0 18 18" aria-hidden="true">
          <circle cx="9" cy="9" r="9" fill="var(--gold)"/>
          <g fill="none" stroke="var(--card-navy)" stroke-width="0.9">
            <circle cx="9" cy="9" r="4.6"/>
            <ellipse cx="9" cy="9" rx="2" ry="4.6"/>
            <path d="M4.4 9h9.2M5 6.8h8M5 11.2h8"/>
          </g>
        </svg>
        <span>www.brennickholdings.com</span>
      </li>
    </ul>

    <address class="address" style="font-style: normal;">
      17, Harbour Row, Suite 4<br>
      20391, Lakeview
    </address>

    <svg class="back-mark" viewBox="0 0 196 196" aria-hidden="true">
      <circle cx="98" cy="98" r="94" fill="none" stroke="var(--gold)" stroke-width="3"/>
    </svg>
  </section>

</main>
</body>
</html>
```